Web Site Design

Lumen Ledgerworks has developed a cloud based accounting systems for small businesses that have out grown products like TallyNest. We are in the process of launching our web site at www.try-lumenly.com. It is hosted on www.pagecradle.com.

Tag Lines:
Simply Innovative Business Management

Cloud Accounting-Anywhere, Anytime, Anyplace

Target Market(s)

Small to med businesses.

Industry/Entity Type

Accounting

Coding

Coded - Design and coding required

Number of Pages Required

5+ page

Font styles to use
Other font styles liked:
• Futura

Requirements
Must have
• I have uploaded graphic pages from a brochure that is being developed.
• I would like to follow the same theme.
• Pages:
• Home Page - Attractive, place holder for ClipHarbor video
• Product Page - Description
• Industries - Discussion of key industries
• Contact
• About

```html
<!DOCTYPE html>
<html lang="en">
<head>
<meta charset="utf-8">
<title>Lumen Ledgerworks — Simply Innovative Business Management</title>
<link rel="stylesheet" href="https://fonts.googleapis.com/css2?family=Jost:wght@400;500;600;700&family=Montserrat:wght@400;600;700;800&display=swap">
<style>
:root{
  --red:#c1272d;
  --red-band:#c4222b;
  --ink:#222222;
  --muted:#444444;
  --soft:#f6f6f6;
  --black:#0a0a0a;
  --footer:#e6e6e6;
  --white:#ffffff;
}
*{box-sizing:border-box;margin:0;padding:0}
html,body{width:1200px;height:3180px;overflow:hidden}
body{background:var(--white);color:var(--ink);font-family:"Jost",Arial,sans-serif}

/* Header */
.site-header{height:113px;position:relative}
.brand{position:absolute;left:112px;top:26px}
.brand-row{display:flex;align-items:center;gap:12px}
.brand-dot{width:48px;height:48px;border-radius:50%;background:var(--red)}
.brand-name{font-family:"Jost",sans-serif;font-weight:500;font-size:30px;color:var(--red);letter-spacing:.5px}
.brand-tag{font-size:13px;color:var(--muted);margin-top:4px}
.main-nav{position:absolute;right:112px;top:50px;display:flex;gap:34px;font-size:17px;font-weight:500}
.main-nav a{color:var(--ink);text-decoration:none}
.main-nav a.active{color:var(--red)}

/* Hero */
.hero{height:542px;position:relative;
  background:radial-gradient(circle at 15% 40%,#c48a52 0,#6b4a35 18%,transparent 40%),
  radial-gradient(circle at 60% 20%,#b9a49a 0,#6f5f5c 25%,transparent 55%),
  linear-gradient(120deg,#3a2a22 0%,#4d3b34 45%,#2b2830 75%,#1c1d24 100%)}
.hero-caption{position:absolute;left:112px;top:222px;width:444px;height:210px;background:rgba(20,20,20,.78);padding:44px 32px}
.hero-caption h1{font-weight:400;font-size:29px;line-height:34px;color:var(--white)}
.hero-arrows{display:flex;gap:6px;margin-top:14px}
.hero-arrows span{width:28px;height:22px;border:1.5px solid var(--white);display:flex;align-items:center;justify-content:center}

/* Sections */
.section-title{font-family:"Montserrat",sans-serif;font-weight:700;font-size:31px;text-align:center;color:var(--ink)}
.services{height:577px;padding-top:58px}
.video{position:relative;width:800px;height:398px;margin:30px auto 0;border:6px solid #d6d6d6;
  background:linear-gradient(110deg,#1f6f9e 0%,#3aa0c8 22%,#8fc6d8 40%,#4b5058 58%,#2b2b2e 80%,#1a1a1c 100%)}
.video-shadow{width:760px;height:30px;margin:0 auto;background:radial-gradient(ellipse at center top,rgba(0,0,0,.35),transparent 70%)}
.play{position:absolute;left:50%;top:50%;transform:translate(-50%,-50%)}

.overview{height:446px;background:var(--soft);padding-top:58px}
.overview p{width:1000px;margin:22px auto 0;font-size:14.5px;line-height:21px;text-align:center;color:var(--ink)}
.overview p + p{margin-top:21px}
.btn{display:block;width:356px;height:57px;margin:36px auto 0;background:#1e1e1e;color:var(--white);font-size:19px;font-weight:500;text-align:center;line-height:57px;border-radius:3px;text-decoration:none}

.features{height:777px;padding-top:48px}
.feature-grid{width:1000px;margin:46px auto 0;display:grid;grid-template-columns:repeat(4,250px);row-gap:44px}
.feature{text-align:center;padding:0 18px}
.feature svg{height:70px;display:block;margin:0 auto}
.feature h3{font-family:"Montserrat",sans-serif;font-weight:700;font-size:14.5px;line-height:20px;margin-top:20px;min-height:42px;display:flex;align-items:center;justify-content:center}
.feature p{font-size:12.5px;line-height:20px;margin-top:14px;color:var(--ink)}

.robust{height:360px;background:var(--red-band);color:var(--white);padding-top:36px}
.robust h2{font-family:"Montserrat",sans-serif;font-weight:400;font-size:48px;line-height:58px;text-align:center}
.robust h2 strong{font-weight:800}
.robust ul{list-style:none;width:1000px;margin:50px auto 0;display:grid;grid-template-columns:repeat(4,250px)}
.robust li{position:relative;padding-left:22px;padding-right:20px;font-family:"Montserrat",sans-serif;font-weight:600;font-size:14.5px;line-height:25px}
.robust li::before{content:"";position:absolute;left:6px;top:8px;border-left:6px solid var(--white);border-top:4.5px solid transparent;border-bottom:4.5px solid transparent}

.cta{height:235px;background:var(--black);color:var(--white);text-align:center;padding-top:56px}
.cta h2{font-family:"Montserrat",sans-serif;font-weight:600;font-size:24px}
.cta a{display:inline-block;width:356px;height:57px;margin-top:24px;background:var(--red);color:var(--white);font-size:19px;font-weight:500;line-height:57px;border-radius:3px;text-decoration:none;letter-spacing:.5px}

.site-footer{height:130px;background:var(--footer);text-align:center;padding-top:26px;font-size:15px}
.site-footer nav a{color:var(--ink);text-decoration:none;margin:0 10px}
.site-footer p{margin-top:28px;font-size:14px}
</style>
</head>
<body>
<header class="site-header">
  <div class="brand">
    <div class="brand-row"><span class="brand-dot"></span><span class="brand-name">Lumen Ledgerworks</span></div>
    <div class="brand-tag">Simply Innovative Business Management</div>
  </div>
  <nav class="main-nav">
    <a class="active" href="#">ABOUT</a><a href="#">PRODUCTS</a><a href="#">READ ME</a><a href="#">CONTACT US</a>
  </nav>
</header>

<section class="hero" role="img" aria-label="Photo of a hand touching a tablet screen with warm blurred lights in the background">
  <div class="hero-caption">
    <h1>Accounting and Business Management Software online business management</h1>
    <div class="hero-arrows">
      <span><svg width="8" height="12" viewBox="0 0 8 12"><path d="M6 1L1 6l5 5" stroke="#fff" stroke-width="2" fill="none"/></svg></span>
      <span><svg width="8" height="12" viewBox="0 0 8 12"><path d="M2 1l5 5-5 5" stroke="#fff" stroke-width="2" fill="none"/></svg></span>
    </div>
  </div>
</section>

<section class="services">
  <h2 class="section-title">Our services</h2>
  <div class="video" role="img" aria-label="Video placeholder: businessman in a suit beside floating financial charts and a world map">
    <svg class="play" width="106" height="106" viewBox="0 0 106 106">
      <circle cx="53" cy="53" r="49" fill="#2a2a2a" stroke="#d9d9d9" stroke-width="5"/>
      <path d="M42 32l32 21-32 21z" fill="#fff"/>
    </svg>
  </div>
  <div class="video-shadow"></div>
</section>

<section class="overview">
  <h2 class="section-title">Overview</h2>
  <p>Lumen Ledgerworks (Lumen) is the first online business management application exclusively written for a smart business. More than just accounting, Lumen provides you with the necessary tools and processes to help your businesses grow. Lumen gets results not just numbers by incorporating many of the principles of the Steadfold Method™ (www.steadfoldmethod.com)*.</p>
  <p>Lumen’s robust features are designed to leverage your company’s greatest asset, it people. Our guiding principle is to simplify the lives of our users while providing your company with the platform it needs to grow. Features like a complete accounting audit trail but with a one click correction to any transaction. You can easily enter and manage a transaction on one screen. No popups or multiple clicks needed, e.g., you can enter a voucher, post it and print a check from one screen. So simple, yet powerful!</p>
  <a class="btn" href="#">LEARN MORE</a>
</section>

<section class="features">
  <h2 class="section-title">Features</h2>
  <div class="feature-grid">
    <div class="feature">
      <svg viewBox="0 0 70 70"><path d="M14 6h26l14 14v44H14z" fill="#c1272d"/><path d="M40 6v14h14" fill="#8f1b20"/><rect x="6" y="14" width="8" height="42" fill="#c1272d"/></svg>
      <h3>Built on the Corvane CRM Platform</h3>
      <p>- Lumen is fully integrated to Corvane CRM. No need to run your accounting on a separate platform and deal with integration tools.</p>
    </div>
    <div class="feature">
      <svg viewBox="0 0 70 70"><rect x="6" y="10" width="58" height="40" rx="3" fill="#c1272d"/><rect x="12" y="16" width="46" height="28" fill="#fff"/><rect x="30" y="50" width="10" height="8" fill="#c1272d"/><rect x="20" y="58" width="30" height="4" fill="#c1272d"/></svg>
      <h3>Full Audit Trail</h3>
      <p>No need to run your accounting on a separate platform and deal with integration tools.</p>
    </div>
    <div class="feature">
      <svg viewBox="0 0 70 70"><path d="M22 18a22 22 0 1 0 26 0" stroke="#c1272d" stroke-width="8" fill="none" stroke-linecap="round"/><line x1="35" y1="8" x2="35" y2="34" stroke="#c1272d" stroke-width="8" stroke-linecap="round"/></svg>
      <h3>One Button Correction</h3>
      <p>Lumen combines simplicity with transparency and a complete audit trail on every transaction</p>
    </div>
    <div class="feature">
      <svg viewBox="0 0 70 70"><circle cx="35" cy="35" r="26" fill="#c1272d"/><path d="M24 22c6 2 8 8 4 12s2 10-4 14M44 30c4 4 2 10 8 12" stroke="#fff" stroke-width="4" fill="none"/></svg>
      <h3>Cloud-Based, Browser Independent</h3>
      <p>Correct a transaction with one click and still maintain an audit trail</p>
    </div>
    <div class="feature">
      <svg viewBox="0 0 70 70"><path d="M14 8h42v30c0 14-12 22-21 26C26 60 14 52 14 38z" fill="#c1272d"/><path d="M35 16v40c-7-4-13-10-13-18V16z" fill="#fff"/></svg>
      <h3>Security to protect your Data</h3>
      <p>Based, Browser Independent - Built on the Corvane CRM Online platform, there is no need to purchase hardware or manage a complex infrastructure. You can securely access Lumen from any standard browser** on your desktop or mobile device.</p>
    </div>
    <div class="feature">
      <svg viewBox="0 0 70 70"><g fill="#c1272d"><path d="M35 6l12 6v12l-12 6-12-6V12z"/><path d="M22 30l12 6v12l-12 6-12-6V36z"/><path d="M48 30l12 6v12l-12 6-12-6V36z"/></g><g stroke="#fff" stroke-width="2" fill="none"><path d="M23 12l12 6 12-6M35 18v12M10 36l12 6 12-6M22 42v12M36 36l12 6 12-6M48 42v12"/></g></svg>
      <h3>Dimensions, Dimensions, Dimensions</h3>
      <p>Lumen utilizes security roles to control access to your company’s data to ensure that users cannot see information or create documents that you don’t want them to.</p>
    </div>
    <div class="feature">
      <svg viewBox="0 0 70 70"><path d="M24 24a11 11 0 1 1 15 10c-3 2-4 4-4 8v4" stroke="#c1272d" stroke-width="8" fill="none"/><rect x="31" y="52" width="9" height="9" fill="#c1272d"/></svg>
      <h3>Advanced Find Queries</h3>
      <p>Lumen provides the ability to tag every transaction with dimension codes that allows you to track projects, events or even repairs to specific activities.</p>
    </div>
    <div class="feature">
      <svg viewBox="0 0 70 70"><g fill="#c1272d"><path d="M8 28h12l30-14v42L20 42H8z"/><path d="M22 44h10l4 14h-10z"/><rect x="54" y="30" width="10" height="10"/></g></svg>
      <h3>Scorecards that Matter*</h3>
      <p>Lumen gives you the ability to slice and dice your data with an easy.</p>
    </div>
  </div>
</section>

<section class="robust">
  <h2><strong>Robust Features</strong> to Help Leverage<br>a Small Business Growth</h2>
  <ul>
    <li>A Flexible, Segmented Chart of Accounts.</li>
    <li>Multi-Location Inventory</li>
    <li>Sales Reporting by Salesperson, Territory or User Defined Dimensions</li>
    <li>Complete 1099 Tracking and Reporting</li>
  </ul>
</section>

<section class="cta">
  <h2>Explore the benefits of Lumen Ledgerworks and grow your business.</h2>
  <a href="#">CONTACT US FOR A DEMO</a>
</section>

<footer class="site-footer">
  <nav><a href="#">About</a>|<a href="#">Products</a>|<a href="#">Read Me</a>|<a href="#">Contact Us</a></nav>
  <p>1180 Harbor Ridge Blvd., Suite 310, Millbrook, MI 48200 &nbsp;| &nbsp;© 2015 Lumen Ledgerworks, LLC - All rights reserved.</p>
</footer>
</body>
</html>
```